Business Card - I already have a Logo

I have a logo, I just want a business card designed that uses it. I would like to see designs that are very clean, have a sense of health and wellbeing, up-market clientele.

Target Market(s)

People interested in health and well-being, people with money! Ages 25-70

Industry/Entity Type

Massage Therapy

Contact Information for Business Card

Tomas Brevin
Integrative Bodyworker

KaHuna, Remedial, Pregnancy & Maya Abdominal Massage, Body Based Psychology. Health fund rebates available
0437615290
info@wenmorestill.com.au

Colors
86cfc6
33b8a4
00a990
85cae6
cee9f5
33a6d7
85acd3
3276b5
0355a3

Requirements
Must have
• Clean, simple, elegant design, using my existing logo

```html
<!DOCTYPE html>
<html lang="en">
<head>
<meta charset="utf-8">
<title>Wenmore Still Massage – Business Card</title>
<link href="https://fonts.googleapis.com/css2?family=Questrial&display=swap" rel="stylesheet">
<style>
  :root {
    --bg: #6f7b8e;
    --card-dark: #232323;
    --card-dark-2: #2e2e2e;
    --white: #ffffff;
    --teal-light: #86cfc6;
    --teal: #33b8a4;
    --sky: #33a6d7;
    --sky-light: #85cae6;
    --blue: #1a8fc8;
    --ink: #f2f2f2;
    --line: #2aa3c4;
  }
  * { box-sizing: border-box; margin: 0; padding: 0; }
  html, body { width: 1200px; height: 810px; overflow: hidden; }
  body {
    background: linear-gradient(180deg, #8a93a3 0%, var(--bg) 100%);
    font-family: "Questrial", "Century Gothic", sans-serif;
    position: relative;
  }
  .card {
    position: absolute;
    top: 255px;
    width: 520px;
    height: 300px;
    border-radius: 4px;
    overflow: hidden;
    box-shadow: 0 18px 40px rgba(20, 28, 45, 0.35);
  }
  .card--front { left: 55px; display: flex; }
  .card--back {
    left: 625px;
    background: linear-gradient(135deg, var(--card-dark-2), var(--card-dark) 70%);
  }

  /* brand lockup */
  .brand { display: flex; align-items: center; gap: 12px; }
  .brand__dot {
    width: 46px; height: 46px; border-radius: 50%;
    background: var(--teal-light);
    flex: none;
  }
  .brand__name {
    color: var(--sky);
    font-size: 22px;
    line-height: 1.05;
    letter-spacing: 0.5px;
  }

  /* front */
  .front__brand-panel {
    width: 205px;
    background: var(--white);
    display: flex; align-items: center; justify-content: center;
    padding: 0 18px;
  }
  .front__brand-panel .brand { flex-direction: column; text-align: center; gap: 10px; }
  .front__divider {
    width: 6px;
    background: linear-gradient(180deg, var(--sky) 0 35%, var(--teal-light) 35% 70%, var(--blue) 70%);
  }
  .front__info {
    flex: 1;
    background: linear-gradient(160deg, var(--card-dark-2), var(--card-dark) 60%);
    padding: 34px 0 0 30px;
    position: relative;
    color: var(--ink);
  }
  .person__name { font-size: 27px; color: var(--white); }
  .person__role { font-size: 14px; color: #d9d9d9; margin-top: 4px; }
  .contacts { margin-top: 24px; list-style: none; }
  .contacts__item {
    display: flex; align-items: center; gap: 12px;
    padding: 8px 0;
    border-bottom: 1px solid var(--line);
    width: 236px;
    font-size: 14px;
  }
  .contacts__item--phone, .contacts__item--email { color: var(--sky-light); }
  .contacts__icon { width: 16px; height: 16px; flex: none; }
  .front__edge {
    position: absolute; right: 0; top: 0; bottom: 0; width: 18px;
    background: linear-gradient(180deg, var(--sky-light) 0 33%, var(--teal) 33% 66%, var(--sky) 66%);
  }

  /* back */
  .back__band {
    position: absolute; left: 0; top: 0; bottom: 0; width: 86px;
    background: linear-gradient(180deg, var(--blue), var(--sky) 55%, #1d86be);
  }
  .back__brand {
    position: absolute; left: 86px; right: 0; top: 0; bottom: 0;
    display: flex; align-items: center; justify-content: center;
  }
  .back__brand .brand__name { font-size: 26px; }
  .back__brand .brand__dot { width: 56px; height: 56px; }
</style>
</head>
<body>

<section class="card card--front" aria-label="Business card front">
  <div class="front__brand-panel">
    <div class="brand">
      <span class="brand__dot" aria-hidden="true"></span>
      <span class="brand__name">Wenmore Still Massage</span>
    </div>
  </div>
  <div class="front__divider" aria-hidden="true"></div>
  <div class="front__info">
    <h1 class="person__name">Tomas Brevin</h1>
    <p class="person__role">Integrative Bodyworker</p>
    <ul class="contacts">
      <li class="contacts__item contacts__item--phone">
        <svg class="contacts__icon" viewBox="0 0 16 16" aria-hidden="true">
          <circle cx="8" cy="8" r="8" fill="#33a6d7"/>
          <rect x="5.5" y="3.5" width="5" height="9" rx="1" fill="none" stroke="#fff" stroke-width="1.2"/>
          <circle cx="8" cy="10.8" r="0.7" fill="#fff"/>
        </svg>
        0437615290
      </li>
      <li class="contacts__item contacts__item--email">
        <svg class="contacts__icon" viewBox="0 0 16 16" aria-hidden="true">
          <circle cx="8" cy="8" r="8" fill="#33a6d7"/>
          <rect x="4" y="5" width="8" height="6" fill="none" stroke="#fff" stroke-width="1.1"/>
          <path d="M4 5 L8 8.5 L12 5" fill="none" stroke="#fff" stroke-width="1.1"/>
        </svg>
        info@wenmorestill.com.au
      </li>
      <li class="contacts__item contacts__item--web">
        <svg class="contacts__icon" viewBox="0 0 16 16" aria-hidden="true">
          <circle cx="8" cy="8" r="8" fill="#33a6d7"/>
          <circle cx="8" cy="8" r="4" fill="none" stroke="#fff" stroke-width="1.1"/>
          <path d="M4 8 H12 M8 4 C6 6 6 10 8 12 M8 4 C10 6 10 10 8 12" fill="none" stroke="#fff" stroke-width="0.9"/>
        </svg>
        www.wenmorestill.com
      </li>
    </ul>
    <div class="front__edge" aria-hidden="true"></div>
  </div>
</section>

<section class="card card--back" aria-label="Business card back">
  <div class="back__band" aria-hidden="true"></div>
  <div class="back__brand">
    <div class="brand">
      <span class="brand__dot" aria-hidden="true"></span>
      <span class="brand__name">Wenmore Still Massage</span>
    </div>
  </div>
</section>

</body>
</html>
```